Landing Page Design for Adult Dating Age Verification (18+)

The objective of this task is to design a visually appealing pre-landing page for the adult dating site "Pivolunda (site: https://pivolunda.example/)" with an age verification mechanism. The pre-landing page will feature two buttons that redirect visitors to the main offer. The design should also include a footer block that includes links to the terms of use, privacy policy, and contact us pages.

Design Requirements:
Develop an age verification section prominently displayed on the pre-landing page.
Design the section to include two buttons labeled "Yes" and "No" for visitors to confirm their age.
Ensure the section is visually appealing and clearly communicates the purpose of age verification.

Visual Appeal:
Create a visually appealing design that aligns with the branding and theme of the "Pivolunda" adult dating site.
Use suitable color schemes, typography, and graphics to enhance the overall visual appeal of the pre-landing page.

Layout and Navigation:
Design an engaging and intuitive layout that encourages visitors to interact with the page and proceed to the main offer.
Ensure clear and visible navigation elements that direct visitors to the main offer or provide additional information.

Responsive Design:
Develop a responsive design that provides a seamless user experience across various devices, including desktop and mobile.
Ensure the design elements and layout adapt well to different screen sizes and resolutions.

File Formats and Assets:
Deliver the final design in PSD, AI, or Sketch format, ensuring that the files are well-organized and layered.
Include any necessary images or assets used in the design, ensuring they are of high quality and optimized for web use.

```html
<!DOCTYPE html>
<html lang="en">
<head>
<meta charset="utf-8">
<title>Pivolunda – Age Check</title>
<link rel="stylesheet" href="https://fonts.googleapis.com/css2?family=Abril+Fatface&family=Montserrat:wght@400&display=swap">
<style>
  :root{
    --page-bg:#1e1a1e;
    --ring:#2a252a;
    --shade:rgba(0,0,0,.62);
    --ink:#0b090b;
    --dim-ink:#0f0d0f;
    --lilac:#d4b8d8;
    --frame:#7a6a7a;
    --white:#ffffff;
    --black:#000000;
  }
  *{margin:0;padding:0;box-sizing:border-box}
  html,body{width:1200px;height:771px;overflow:hidden;background:var(--page-bg)}
  .canvas{position:relative;width:1200px;height:771px;overflow:hidden;background:var(--page-bg);font-family:"Abril Fatface",serif}

  .ring{position:absolute;left:600px;top:0;width:530px;height:530px;border-radius:50%;background:var(--ring)}
  .header-brand{position:absolute;left:102px;top:8px;display:flex;align-items:center;gap:10px;font-size:27px;color:var(--dim-ink)}
  .header-brand .dot{width:30px;height:30px;border-radius:50%;background:#3a303a}
  .eyebrow{position:absolute;left:112px;top:104px;font-size:16px;letter-spacing:1px;color:#2b262b}
  .hero-title{position:absolute;left:112px;top:148px;font-size:43px;line-height:52px;font-weight:400;letter-spacing:1px;color:var(--dim-ink)}
  .hero-cta{position:absolute;left:112px;top:296px;width:200px;height:62px;border-radius:31px;background:#2b252b;color:#3c343c;font-size:14px;letter-spacing:1px;padding:22px 0 0 20px}
  .hero-sub{position:absolute;left:112px;top:636px;font-size:68px;letter-spacing:1px;color:var(--dim-ink)}
  .shade{position:absolute;inset:0;background:var(--shade)}

  .model-photo{position:absolute;left:805px;top:56px;width:300px;height:658px;border-radius:150px 150px 20px 20px;background:linear-gradient(180deg,#e8c79a 0%,#e9bfa8 35%,#d9a88f 70%,#c99682 100%)}

  .age-modal{position:absolute;z-index:2;left:224px;top:213px;width:581px;height:346px;border:8px solid var(--frame);background:var(--white);border-radius:4px;text-align:center}
  .modal-brand{display:flex;justify-content:center;align-items:center;gap:12px;margin-top:70px;font-size:30px;line-height:36px;color:var(--ink)}
  .modal-brand .dot{width:36px;height:36px;border-radius:50%;background:var(--lilac)}
  .age-question{margin-top:24px;font-size:31px;line-height:38px;letter-spacing:1.6px;color:var(--ink)}
  .age-actions{display:flex;justify-content:center;gap:8px;margin-top:28px}
  .age-btn{width:179px;height:54px;border:0;font-family:"Abril Fatface",serif;font-size:29px;letter-spacing:1px;color:var(--white)}
  .age-btn.yes{background:var(--black)}
  .age-btn.no{background:var(--lilac)}

  .site-footer{position:absolute;z-index:3;left:0;top:714px;width:1200px;height:57px;background:var(--lilac);display:flex;justify-content:center;align-items:center;gap:20px;font-family:"Montserrat",sans-serif;font-size:17px;letter-spacing:.3px;color:#2a232a}
</style>
</head>
<body>
<div class="canvas">
  <div class="ring"></div>
  <div class="header-brand"><span class="dot"></span>Pivolunda</div>
  <div class="eyebrow">PIVOLUNDA</div>
  <h1 class="hero-title">The best advisor<br>in the dating world</h1>
  <div class="hero-cta">UNLOCK MATCHES</div>
  <div class="hero-sub">Meet your dream</div>
  <div class="shade"></div>

  <div class="model-photo" role="img" aria-label="Photo of a blonde woman in a black bikini posing"></div>

  <div class="age-modal" role="dialog" aria-label="Age verification">
    <div class="modal-brand"><span class="dot"></span>Pivolunda</div>
    <p class="age-question">Are you of legal dating age?</p>
    <div class="age-actions">
      <button class="age-btn yes">Yes</button>
      <button class="age-btn no">No</button>
    </div>
  </div>

  <footer class="site-footer">
    <span>PRIVACY POLICY</span><span>|</span><span>TERMS AND CONDITIONS</span><span>|</span><span>CANCEL SUBSCRIPTION</span>
  </footer>
</div>
</body>
</html>
```